Medical Billing - Professional Marketing Flier

We are needing help designing a clean and professional looking easy to read marketing flier for a medical billing practice. The text needs to be large enough to print. We are looking for a 5.5 x 8.5 design that we can edit the text as needed. I have included our logo and what we initially want it to say. Please keep in mind, we also want our logo and contact details on the flier. Let me know if you have any questions.

```html
<!DOCTYPE html>
<html lang="en">
<head>
<meta charset="utf-8">
<title>Vega Medical Billing – Flier</title>
<link href="https://fonts.googleapis.com/css2?family=Tinos:wght@400;700&display=swap" rel="stylesheet">
<style>
:root{
  --ink:#111;
  --black:#000;
  --white:#fff;
  --purple:#6a3c9c;
  --purple-deep:#4a1a6e;
  --gold:#fcc947;
  --gold-deep:#f0a930;
  --shadow:#8a8a8a;
  --photo-blue:#8fb4d6;
}
*{margin:0;padding:0;box-sizing:border-box}
html,body{width:857px;height:1200px;overflow:hidden;background:var(--white)}
.flier{position:relative;width:857px;height:1200px;overflow:hidden;font-family:"Tinos","Times New Roman",serif;color:var(--ink);background:var(--black)}
.backdrop{position:absolute;left:0;top:0}
.brand{position:absolute;left:56px;top:86px;width:292px;text-align:center;color:var(--purple);font-weight:400}
.brand-name{font-size:58px;letter-spacing:2px;line-height:1}
.brand-sub{font-size:14px;letter-spacing:4px;margin-top:6px}
.brand-dot{display:inline-block;width:12px;height:12px;border-radius:50%;background:var(--purple);margin-right:10px;vertical-align:middle}
.headline{position:absolute;left:34px;top:205px;font-size:33px;font-weight:700;line-height:46px;color:var(--ink)}
.hero-photo{position:absolute;left:433px;top:-54px;width:452px;height:452px;border-radius:50%;border:22px solid var(--gold);box-shadow:0 0 0 3px var(--gold-deep);background:radial-gradient(circle at 55% 45%,#eef2f6 0%,#c9d6e3 45%,var(--photo-blue) 100%)}
.service{position:absolute;left:0;width:857px;height:180px}
.service-card{position:absolute;left:141px;top:28px;width:699px;height:140px;background:var(--white);border-radius:0 70px 70px 0;box-shadow:5px 6px 0 var(--shadow)}
.service-tab{position:absolute;left:190px;top:0;width:220px;height:42px;background:linear-gradient(#ffd866,var(--gold));box-shadow:3px 3px 0 var(--shadow);font-weight:700;font-size:16px;text-align:center;line-height:42px;color:var(--ink);z-index:2}
.service-text{position:absolute;left:82px;top:16px;width:578px;font-size:13px;line-height:17.9px;text-align:justify;text-indent:200px}
.service-photo{position:absolute;left:26px;top:-3px;width:178px;height:178px;border-radius:50%;border:7px solid var(--white);box-shadow:4px 4px 0 var(--shadow);z-index:3}
.photo-steth{background:linear-gradient(135deg,#e6edf3,#b8c6d3 60%,#7f93a6)}
.photo-blocks{background:linear-gradient(135deg,#5fa1c8,#2a6d98 60%,#d8b894)}
.photo-pen{background:linear-gradient(135deg,#f4f7fb,#bcd6ea 60%,#4f8fc9)}
.contact{position:absolute;left:40px;top:962px;width:777px;text-align:center;color:var(--white)}
.contact h2{font-size:22px;font-weight:700;margin-bottom:5px}
.contact p{font-size:16.5px;font-weight:700;line-height:21.5px}
.footer{position:absolute;left:0;top:1096px;width:857px;height:104px;border-top:5px solid var(--gold-deep);background:linear-gradient(var(--purple),var(--purple-deep));color:var(--white);font-weight:700;font-size:21px;text-align:center;padding-top:14px}
.footer-row{display:flex;justify-content:center;align-items:center;gap:12px;height:36px}
.footer-item{display:flex;align-items:center;gap:8px}
.icon{width:28px;height:28px}
</style>
</head>
<body>
<main class="flier">
  <svg class="backdrop" viewBox="0 0 857 1200" width="857" height="1200" aria-hidden="true">
    <defs>
      <linearGradient id="swoosh" x1="0" x2="1" y1="0" y2="0">
        <stop offset="0" stop-color="#8a66b8"/>
        <stop offset="1" stop-color="#5d2b8a"/>
      </linearGradient>
    </defs>
    <rect width="857" height="1200" fill="#000"/>
    <path d="M0 402 C150 418 300 398 450 356 C570 322 700 300 857 328 V392 C700 372 520 392 380 420 C250 446 120 470 0 482 Z" fill="url(#swoosh)"/>
    <path d="M0 500 C60 520 100 540 140 552" stroke="#b07ad8" stroke-width="2" fill="none"/>
    <path d="M0 0 H857 V230 L620 250 C540 320 420 380 240 385 C140 388 60 376 0 362 Z" fill="#fff"/>
  </svg>

  <div class="brand">
    <div class="brand-name"><span class="brand-dot"></span>VEGA</div>
    <div class="brand-sub">MEDICAL BILLING</div>
  </div>

  <h1 class="headline">Medical Billing<br>Tailored To Your<br>Practices Needs</h1>

  <div class="hero-photo" role="img" aria-label="Photo of a nurse in blue scrubs writing on a clipboard beside a patient in bed"></div>

  <section class="service" style="top:389px">
    <div class="service-photo photo-steth" role="img" aria-label="Photo of a stethoscope resting on an ECG chart"></div>
    <div class="service-tab">MEDICAL BILLING</div>
    <div class="service-card">
      <p class="service-text">Would you prefer to spend time focusing on your clients and running your practice rather than trying to stay up to speed with the constantly changing medical billing rules and regulations? Let us help you by managing your medical billing and dealing with the insurance companies on your behalf! We work with you to tailor the entire medical billing process to suit your practices needs while making it as smooth and painless as possible.</p>
    </div>
  </section>

  <section class="service" style="top:585px">
    <div class="service-photo photo-blocks" role="img" aria-label="Photo of a hand stacking wooden blocks with medical symbols"></div>
    <div class="service-tab">AGING</div>
    <div class="service-card">
      <p class="service-text">Are you leaving money on the table? Are you able to do the follow-through needed to keep your aging in check and more money flowing into your practice? Are you uncertain about how to get insurance to pay on claims that should be covered but for some reason they decided not to? We can clean up your aging, reduce the amount of time it takes for claims to pay out, and we can keep your aging to a minimum.</p>
    </div>
  </section>

  <section class="service" style="top:781px">
    <div class="service-photo photo-pen" role="img" aria-label="Photo of a hand writing with a pen next to a stethoscope"></div>
    <div class="service-tab">CREDENTIALING</div>
    <div class="service-card">
      <p class="service-text">Are you wanting to get contracted with insurance companies but aren’t sure how to go about it? Are you wanting to expand your client base by having the option to bill insurance? Let us take the confusion out of what can seem like a daunting task! We can get you and your practitioners contracted with the insurance companies of your choice and help you navigate through the process every step of the way!</p>
    </div>
  </section>

  <section class="contact">
    <h2>CONTACT US</h2>
    <p>If any of these processes are something you would like our help with or to consult with us on, please email us or give us a call! We specialize in billing and contracting for Nutritionists and Dietitians. We would love to help you expand your business and take the pain and frustration out of billing so you can focus on your clients.</p>
  </section>

  <footer class="footer">
    <div class="footer-row">
      <span class="footer-item">
        <svg class="icon" viewBox="0 0 26 26" aria-hidden="true"><circle cx="13" cy="13" r="12" fill="#fcc947"/><path d="M8 7 L11 7 L12 10 L10.5 11.5 C11.5 13.5 12.5 14.5 14.5 15.5 L16 14 L19 15 L19 18 C13 19 7 13 8 7Z" fill="#4a1a6e"/></svg>
        555-014-2287
      </span>
      <span class="footer-item" style="margin-left:14px">
        <svg class="icon" viewBox="0 0 26 26" aria-hidden="true"><rect x="1" y="3" width="24" height="20" rx="5" fill="#fcc947"/><rect x="6" y="8" width="14" height="10" fill="none" stroke="#4a1a6e" stroke-width="1.8"/><path d="M6 8 L13 14 L20 8" fill="none" stroke="#4a1a6e" stroke-width="1.8"/></svg>
        admin@vegamedicalbilling.com
      </span>
    </div>
    <div class="footer-row">
      <span class="footer-item">
        <svg class="icon" viewBox="0 0 26 26" aria-hidden="true"><circle cx="13" cy="13" r="12" fill="#fcc947"/><path d="M13 5 C9.5 5 7.5 7.5 7.5 10.5 C7.5 14 13 20 13 20 C13 20 18.5 14 18.5 10.5 C18.5 7.5 16.5 5 13 5Z" fill="#4a1a6e"/><circle cx="13" cy="10.5" r="2.2" fill="#fcc947"/></svg>
        P.O. Box-412, Maple Falls, WA-98000.
      </span>
    </div>
  </footer>
</main>
</body>
</html>
```